Simple and clean poster/flyer design needed for public speaker!

SIMPLE AND CLEAN DESIGN NEEDED FOR POSTER/FLYER

I AM a public speaker based in London (www.corvanlethby.com)
and I would like to have a custom-made flyer/poster
(preferably in adobe CS4 template format) that I con customize (just changing the text) for my various speeches, topics and locations

I am looking for something very simple and clean.
NO extravagance or crowded poster, but a rather beautiful clean and eye-catching design that clearly informs people what i am talking about, where and when.

Go to my website www.corvanlethby.com
to see the colour scheme and style that I like
my poster should be like the website, similar colours, logo, clean, simple and clear.

Summary

(1) simple and clean design
(2) design that fits my brand (see website)
(3) clear and eye-catching to promote my speeches
(4) customizable for my various talks, by simply chancing the text (Please Adobe Photoshop CS4 template format)
(5)in A3, A4, A5, A6 sizes, so i can use it for both flyers and small posters

ADDITIONS

BIG BOLD HEADLINE TO GRAP ATTENTION, greatest prominence

sub headline to explain, smaller than the headline, but still prominent on the poster

just a few bullet points to list the benefits and answer the “whats in for me”-question
this is for people who are already interested and continue reading, medium prominence.

WHERE, WHEN, HOW MUCH-information, in the lower section of the poster, little text, but clearly visible

only one point of CONTACT on my poster “www.corvanlethby.com”, bit big and clear so that it is very prominent

little text, effectively used
LESS IS MORE
Updates

contact me regarding logo files and any questions you may have!

for the logo files go to

https://share.dropvaultex.net/f/x.aspx?k=41c07d2e9ab35f18c6d2

click on the folder "logo pack" to see the files

thanks for your interest. hope to see great designs!
I am really looking forward to it
if you have any questions, please do not hesitate to ask

Kind Regards
Corvan
 

• Simple, clean design, text sparingly used.

• The mood should be light-hearted, calm, bright, simple and friendly, comic like

• a lot of white space, calling more attention to the content

• a light blue, dark blue, white and black colour scheme as seen on the homepage (www.corvanlethby.com) please use the exact same colours as seen on the homepage.

White being most predominant, 2 different blue used to highlight something, black for text on white background.

• One graphic would be cool, as long as it is blue. It could be waves-like graphic, or something like the white pattern in the background, in my case just in blue on white background > http://www.quillmereretreathouse.org/., I do not mean exactly this graphic and not that crowded but a simple single graphic in blue as long as it fits the theme and feel of my poster

Top o f the poster

• (a )One short bold headline (TALK TITLE) with a sub-headline below it (hook)

• or (b) headline as question (…....?) and below sub-headline offering the solution (my talk ;-) of course)

• 3 benefits as on homepage, that I can adapt for each talk (bottom right of my start site “what are you looking for?” either blue on white, or as in the page white on blue...whatever looks better and fits the design). Not sure how that looks, and if to include it!

• the bottom of the poster will have “Where”-information “when”-information “ticket price” info

• contact at the very bottom...for more into or to purchase tickets (my website and email)

If you have any questions or need clarification please write me!

Requirements
Must have
• lot of white space
• less is more - simple design
• little text, little graphics- only used when necessary to greatest effect.
• light, friendly, modern feel
• blue-color scheme

```html
<!DOCTYPE html>
<html lang="en">
<head>
<meta charset="utf-8">
<title>Corvan Lethby – Talk Poster</title>
<link rel="stylesheet" href="https://fonts.googleapis.com/css2?family=Arimo:wght@700&family=EB+Garamond:ital@0;1&family=Great+Vibes&family=Roboto+Condensed:wght@400;700&display=swap">
<style>
  :root {
    --sky-top: #b7d8e4;
    --sky-mid: #e6f3f8;
    --paper: #ffffff;
    --slate: #566b76;
    --slate-soft: #8d9ea6;
    --ink: #3d4f5c;
    --brand-blue: #1f8fc4;
    --brand-dark: #243746;
    --band-light: #8fcbe0;
    --band-mid: #4fa3cf;
    --band-deep: #2a72b0;
    --white: #ffffff;
  }
  * { margin: 0; padding: 0; box-sizing: border-box; }
  html, body { width: 1008px; height: 1200px; overflow: hidden; background: var(--paper); }
  .poster {
    position: relative;
    width: 1008px;
    height: 1200px;
    overflow: hidden;
    background:
      radial-gradient(ellipse 70% 45% at 55% 52%, var(--paper) 0%, rgba(255,255,255,0) 100%),
      linear-gradient(180deg, var(--sky-top) 0%, var(--sky-mid) 32%, var(--paper) 60%);
  }
  .headline-block { position: absolute; left: 78px; top: 212px; }
  .brace {
    position: absolute; left: 0; top: -22px;
    font-family: "EB Garamond", serif; font-size: 190px; line-height: 1;
    color: var(--slate); font-weight: 400;
    transform: scaleX(0.55); transform-origin: left top;
  }
  .headline {
    position: absolute; left: 71px; top: 30px; white-space: nowrap;
    font-family: "Arimo", sans-serif; font-weight: 700; font-size: 52px;
    color: var(--slate); letter-spacing: 0.5px;
  }
  .subheadline {
    position: absolute; left: 71px; top: 96px; white-space: nowrap;
    font-family: "EB Garamond", serif; font-size: 31px; color: var(--slate);
  }
  .benefits { position: absolute; left: 134px; top: 490px; }
  .question {
    font-family: "Roboto Condensed", sans-serif; font-weight: 700;
    font-size: 35px; color: var(--slate); white-space: nowrap;
  }
  .question .mark {
    font-family: "EB Garamond", serif; font-size: 52px; vertical-align: 14px; line-height: 0;
  }
  .benefit-list { list-style: none; margin: 18px 0 0 17px; }
  .benefit-list li {
    font-family: "EB Garamond", serif; font-style: italic;
    font-size: 29px; line-height: 39px; color: var(--slate-soft);
  }
  .brand {
    position: absolute; left: 62px; top: 790px;
    display: flex; align-items: center; gap: 14px;
  }
  .brand-dot { width: 64px; height: 64px; border-radius: 50%; background: var(--brand-blue); }
  .brand-name {
    font-family: "Roboto Condensed", sans-serif; font-weight: 400;
    font-size: 30px; color: var(--brand-dark); text-transform: uppercase; letter-spacing: 0.5px;
  }
  .info-band {
    position: absolute; left: 0; top: 857px; width: 1008px; height: 343px;
    background:
      radial-gradient(ellipse 50% 60% at 55% 35%, rgba(180,228,242,0.7) 0%, rgba(180,228,242,0) 100%),
      linear-gradient(180deg, var(--band-light) 0%, var(--band-mid) 55%, var(--band-deep) 100%);
  }
  .tagline {
    position: absolute; left: 0; top: 860px; width: 1008px; text-align: center;
    font-family: "Arimo", sans-serif; font-weight: 700; font-size: 58px;
    color: var(--white); letter-spacing: 1px;
    text-shadow: 2px 3px 4px rgba(20,50,80,0.55);
  }
  .event-details { position: absolute; left: 151px; top: 944px; }
  .event-details p {
    font-family: "Roboto Condensed", sans-serif; color: var(--ink);
    font-size: 32px; line-height: 49px; white-space: nowrap;
  }
  .event-details .label { font-weight: 700; font-size: 25px; }
  .event-details .cents { font-size: 20px; }
  .contact-intro {
    position: absolute; left: 156px; top: 1086px; white-space: nowrap;
    font-family: "EB Garamond", serif; font-style: italic; font-size: 31px; color: var(--white);
  }
  .contact-intro .dash { display: inline-block; width: 60px; height: 3px; background: var(--white); vertical-align: 8px; margin: 0 8px; border-radius: 2px; }
  .contact-line {
    position: absolute; left: 153px; top: 1132px; white-space: nowrap;
    font-family: "Arimo", sans-serif; font-weight: 700; font-size: 20px; color: var(--white);
  }
  .contact-line .or {
    font-family: "Great Vibes", cursive; font-weight: 400; font-size: 30px; margin: 0 18px;
  }
</style>
</head>
<body>
<main class="poster">
  <section class="headline-block">
    <span class="brace">}</span>
    <h1 class="headline">One Short Bold Headline.</h1>
    <h2 class="subheadline">a sub-headline below it a sub-headline below it</h2>
  </section>

  <section class="benefits">
    <p class="question"><span class="mark">“</span>what are you looking for?<span class="mark">”</span></p>
    <ul class="benefit-list">
      <li>3 benefits as on homepage</li>
      <li>3 benefits as on homepage</li>
      <li>3 benefits as on homepage</li>
    </ul>
  </section>

  <div class="brand">
    <span class="brand-dot"></span>
    <span class="brand-name">Corvan Lethby</span>
  </div>

  <div class="info-band" role="img" aria-label="Blue band with soft swirl ornaments and flowing wave lines"></div>

  <p class="tagline">simple . universal . powerful</p>

  <section class="event-details">
    <p><span class="label">Date:</span> September 15th, 2010</p>
    <p><span class="label">Location:</span> location, location, location</p>
    <p><span class="label">Ticket Price :</span> $00.<span class="cents">00</span></p>
  </section>

  <p class="contact-intro">for more information<span class="dash"></span>or to purchase tickets:</p>
  <p class="contact-line">contact@corvanlethby.com<span class="or">or</span>www.corvanlethby.com</p>
</main>
</body>
</html>
```